Billboard design for agricultural machinery business

hello im looking for roadside advertiement sign to be designed, the sign is 10ft up in the air and is 4ft high and 8ft wide, id image i like a blue background and my logo front and centre and below logo sales - service - parts and then below that the brook meadow symbol and vale symbol, I’d also like the website www.Fernowell.ie on it. i am open to suggestions and designs. blue is #005999 and yellow is rgb (254, 205, 26) ive attached my log and symbols, im open to different colour backgrounds or just white and also open to brook meadow and vale as writhing rather than logos

Target Market(s)

Brook Meadow and vale tractor owners

Industry/Entity Type

Agricultural machine sales service and parts

Colors

Designer to choose colors to be used in the design.

Requirements
Must have
• My logo and colours, brands brook Meadow and vale, website

```html
<!DOCTYPE html>
<html lang="en">
<head>
<meta charset="utf-8">
<title>Fernowell Roadside Billboard</title>
<link rel="stylesheet" href="https://fonts.googleapis.com/css2?family=Montserrat:wght@600;700;800&display=swap">
<style>
  :root {
    --brand-blue: #005999;
    --brand-yellow: rgb(254, 205, 26);
    --paper: #ffffff;
    --ink: #1d1d1b;
    --accent-red: #c1392b;
    --stage: #c9ccd1;
  }
  * { box-sizing: border-box; margin: 0; padding: 0; }
  html, body {
    width: 1200px;
    height: 850px;
    overflow: hidden;
  }
  body {
    background: var(--stage);
    font-family: "Montserrat", Arial, sans-serif;
    position: relative;
  }
  .billboard {
    position: absolute;
    left: 40px;
    top: 145px;
    width: 1120px;
    height: 559px;
    background: var(--brand-blue);
    overflow: hidden;
  }
  .billboard__base {
    position: absolute;
    inset: 0;
    width: 100%;
    height: 100%;
  }
  .brand-name {
    position: absolute;
    left: 0;
    right: 0;
    top: 112px;
    display: flex;
    justify-content: center;
    align-items: center;
    gap: 14px;
    color: var(--paper);
    font-weight: 800;
    font-size: 62px;
    letter-spacing: 0.5px;
    line-height: 1;
  }
  .brand-name__dot {
    width: 22px;
    height: 22px;
    border-radius: 50%;
    background: var(--brand-yellow);
  }
  .services {
    position: absolute;
    left: 0;
    right: 0;
    top: 250px;
    display: flex;
    justify-content: center;
    align-items: center;
    gap: 26px;
    color: var(--paper);
    font-weight: 800;
    font-size: 84px;
    line-height: 1;
    letter-spacing: -0.5px;
  }
  .services__dot {
    width: 24px;
    height: 24px;
    border-radius: 50%;
    background: var(--brand-yellow);
    margin-top: 12px;
  }
  .contact {
    position: absolute;
    left: 0;
    right: 0;
    top: 405px;
    text-align: center;
    color: var(--brand-blue);
  }
  .contact__phone {
    font-weight: 700;
    font-size: 56px;
    line-height: 1;
    letter-spacing: 1px;
  }
  .contact__web {
    margin-top: 10px;
    font-weight: 700;
    font-size: 42px;
    line-height: 1;
  }
  .partner {
    position: absolute;
    top: 458px;
    display: flex;
    align-items: center;
    gap: 10px;
    font-weight: 800;
    font-size: 30px;
    line-height: 1;
  }
  .partner__mark {
    width: 22px;
    height: 22px;
  }
  .partner--brook-meadow {
    left: 60px;
    color: var(--brand-blue);
  }
  .partner--brook-meadow .partner__mark { background: var(--brand-yellow); }
  .partner--vale {
    right: 80px;
    color: var(--ink);
    font-size: 46px;
    top: 448px;
  }
  .partner--vale .partner__mark { background: var(--accent-red); }
</style>
</head>
<body>
  <main class="billboard">
    <svg class="billboard__base" viewBox="0 0 1120 559" preserveAspectRatio="none" aria-hidden="true">
      <path d="M0,423 Q560,331 1120,423 L1120,559 L0,559 Z" fill="var(--brand-yellow)"/>
      <path d="M0,441 Q560,341 1120,441 L1120,559 L0,559 Z" fill="var(--paper)"/>
    </svg>

    <div class="brand-name">
      <span>Fernowell</span>
      <span class="brand-name__dot"></span>
    </div>

    <h1 class="services">
      <span>Sales</span>
      <span class="services__dot"></span>
      <span>Service</span>
      <span class="services__dot"></span>
      <span>Parts</span>
    </h1>

    <div class="contact">
      <p class="contact__phone">0851 370 914</p>
      <p class="contact__web">www.fernowell.ie</p>
    </div>

    <div class="partner partner--brook-meadow">
      <span class="partner__mark"></span>
      <span>Brook Meadow</span>
    </div>

    <div class="partner partner--vale">
      <span>VALE</span>
      <span class="partner__mark"></span>
    </div>
  </main>
</body>
</html>
```